Letterhead, envelope, business card design

I am looking to update the communication materials for our Association and Foundation. We have two organization (Pine Ridge Bar Association (the membership organization for lawyers and judges) and the Pine Ridge Bar Foundation (the charitable arm of our organization).

I am attaching copies of the two organizations logos.

I am looking to update the following pieces:
* our current versions are attached for your review
* the image conveyed should be sophisticated
* Our organization color is reflex blue (I don't think the Foundation logo is correct in the versions I have)

Association:
(1) 8.5" x 11" letterhead (page 1)
(2) #10 envelopes (page 2)
(3) note cards (page 3)
(4) note card envelope (page 4)

Foundation:
(5) 8.5" x 11" letterhead (page 5)
(6) #10 envelopes (page 6)
(7) note cards (page 7)
(8) note card envelope (page 8)

Joint Association and Foundation: (using both logos)
(9) 7.5" x 10.5" (monarch) letterhead (no current version)
(10) Monarch envelope (no current version)
(11) two sided business card (page 9)

FUTURE PROJECTS:
** Membership form (tri-fold 8.5" x 11" )(page 11&12)
** Foundation overview brochure (bi-fold 8.5" x 11") (page13&14)

Target Market(s)

Lawyers and Judges

Industry/Entity Type

Business

Font styles to use
Serif

Requirements
Must have
• Street Address, City, State, Zip, Phone, web address
Nice to have
• .
Should not have
• no clip art, no additional images other than logos

```html
<!DOCTYPE html>
<html lang="en">
<head>
<meta charset="utf-8">
<title>Pine Ridge Bar Association – Stationery</title>
<link href="https://fonts.googleapis.com/css2?family=Source+Serif+4:opsz,wght@8..60,400;8..60,600;8..60,700&display=swap" rel="stylesheet">
<style>
  :root {
    --bg: #858c98;
    --blue: #0f4c9e;
    --blue-light: #2a66b3;
    --blue-deep: #0b3f86;
    --grey-box: #555759;
    --paper: #ffffff;
    --ink: #3a3a3a;
  }
  * { box-sizing: border-box; margin: 0; padding: 0; }
  html, body { width: 1200px; height: 872px; overflow: hidden; }
  body {
    background: var(--bg);
    font-family: "Source Serif 4", serif;
    color: var(--ink);
    position: relative;
  }
  .piece { position: absolute; background: var(--paper); box-shadow: 0 3px 10px rgba(0,0,0,0.25); overflow: hidden; }

  /* Brand name block */
  .brand { display: flex; align-items: center; gap: 6px; color: var(--blue); font-weight: 600; letter-spacing: 0.05em; text-transform: uppercase; line-height: 1.1; white-space: nowrap; }
  .brand-dot { width: 10px; height: 10px; border-radius: 50%; background: var(--blue); flex: none; }

  /* Contact box */
  .contact-box { position: absolute; background: var(--grey-box); color: #fff; display: flex; gap: 10px; padding: 6px 8px; font-size: 5.5px; line-height: 1.4; }
  .contact-box .org { font-weight: 700; text-transform: uppercase; font-size: 6px; letter-spacing: 0.03em; }
  .contact-box .col { flex: 1; }
  .contact-box .divider { width: 1px; background: rgba(255,255,255,0.6); }

  /* Folder */
  .folder { left: 300px; top: 40px; width: 380px; height: 500px; background: linear-gradient(160deg, var(--blue-light), var(--blue-deep)); }
  .folder-band { position: absolute; left: 0; right: 0; bottom: 110px; height: 70px; background: var(--paper); display: flex; align-items: center; padding-left: 30px; }
  .folder-band .brand { font-size: 13px; }

  /* Letterhead */
  .letterhead { left: 720px; top: 40px; width: 420px; height: 543px; }
  .lh-square { position: absolute; left: 30px; top: 0; width: 34px; height: 34px; background: var(--blue); }
  .lh-brand { position: absolute; left: 170px; top: 22px; font-size: 11px; }
  .letterhead .contact-box { right: 0; top: 74px; width: 200px; }
  .letter { position: absolute; left: 40px; top: 120px; width: 300px; font-size: 7.5px; line-height: 1.45; }
  .letter p { margin-bottom: 7px; }
  .signature { position: absolute; left: 230px; top: 430px; width: 80px; height: 32px; background: linear-gradient(90deg, #f1f2f4, #e4e6ea); border-radius: 3px; }
  .lh-band { position: absolute; left: 0; right: 0; bottom: 0; height: 5px; background: var(--blue); }

  /* Business cards */
  .card { left: 40px; width: 230px; height: 131px; border-bottom: 4px solid var(--blue); }
  .card--back { top: 60px; }
  .card--front { top: 215px; display: flex; align-items: center; justify-content: center; }
  .card--front .brand { font-size: 11px; }
  .card--back .brand { position: absolute; left: 50px; top: 26px; font-size: 9px; }
  .card--back .contact-box { left: 0; right: 0; bottom: 0; }

  /* Envelopes */
  .envelope { top: 620px; width: 480px; height: 208px; }
  .envelope--front { left: 40px; }
  .env-square { position: absolute; left: 20px; top: 0; width: 22px; height: 22px; background: var(--blue); }
  .envelope--front .brand { position: absolute; left: 50px; top: 18px; font-size: 9px; }
  .envelope--front .contact-box { right: 0; top: 60px; width: 180px; }
  .envelope--back { left: 560px; }
  .env-flap { position: absolute; left: 0; right: 0; top: 70px; height: 58px; background: var(--blue); }
</style>
</head>
<body>

  <section class="piece folder" aria-label="Presentation folder">
    <div class="folder-band">
      <div class="brand"><span class="brand-dot"></span>Pine Ridge Bar Association</div>
    </div>
  </section>

  <section class="piece letterhead" aria-label="Letterhead">
    <div class="lh-square"></div>
    <div class="brand lh-brand"><span class="brand-dot"></span>Pine Ridge Bar Association</div>
    <div class="contact-box">
      <div class="col"><div class="org">Pine Ridge Bar Association</div>2140 Alder Court, Suite 4<br>Pine Ridge, CA 95310</div>
      <div class="divider"></div>
      <div class="col">Telephone (555) 014-2270<br>Fax (555) 014-2271<br>Web pineridgebar.org</div>
    </div>
    <div class="letter">
      <p>2140 Alder Court<br>Pine Ridge, CA 95310</p>
      <p>January 20th, 2011</p>
      <p>Mr. Harlow<br>President, Harlow Youth Center<br>58 Meadow Lane<br>Pine Ridge, CA 95312</p>
      <p>Dear Mr. Harlow:</p>
      <p>In the first paragraph, one needs to give a brief introduction of oneself. One should also give reference to the purpose of the letter in brief. The second paragraph needs to give the details of the letter and its need. This paragraph is mostly longer than the others and plays the main role in the letter. Keep the sentences short and to the point. Avoid using complex words and sentences.</p>
      <p>The third and last paragraph is the conclusion of the letter and can be kept short.</p>
      <p>Sincerely,</p>
      <p>(this is where the signature of the writer will be placed)</p>
      <p>Dana Whitfield<br>Read more at Letterwise: www.letterwise.example/letter-format</p>
    </div>
    <div class="signature" role="img" aria-label="Handwritten signature"></div>
    <div class="lh-band"></div>
  </section>

  <section class="piece card card--back" aria-label="Business card back">
    <div class="brand"><span class="brand-dot"></span>Pine Ridge Bar Association</div>
    <div class="contact-box">
      <div class="col"><div class="org">Pine Ridge Bar Association</div>2140 Alder Court, Suite 4<br>Pine Ridge, CA 95310</div>
      <div class="divider"></div>
      <div class="col">Telephone (555) 014-2270<br>Fax (555) 014-2271<br>Web pineridgebar.org</div>
    </div>
  </section>

  <section class="piece card card--front" aria-label="Business card front">
    <div class="brand"><span class="brand-dot"></span>Pine Ridge Bar Association</div>
  </section>

  <section class="piece envelope envelope--front" aria-label="Envelope front">
    <div class="env-square"></div>
    <div class="brand"><span class="brand-dot"></span>Pine Ridge Bar Association</div>
    <div class="contact-box">
      <div class="col"><div class="org">Pine Ridge Bar Association</div>2140 Alder Court, Suite 4<br>Pine Ridge, CA 95310</div>
      <div class="divider"></div>
      <div class="col">Telephone (555) 014-2270<br>Fax (555) 014-2271<br>Web pineridgebar.org</div>
    </div>
  </section>

  <section class="piece envelope envelope--back" aria-label="Envelope back">
    <div class="env-flap"></div>
  </section>

</body>
</html>
```